Neudesign Homepage für Computerfirma
Zielgruppe
Wir sind ein seit 12 Jahren lokal ansässiger EDV Dienstleister mit Verkauf von PC, Notebooks etc. mit eigener Reparaturwerkstätte, Handel mit Computerzubehör. Zielgruppe: Klein- bis mittelständige Unternehmen / Organisationen, sowie Privatpersonen aller Altersgruppen.
Aufgabenstellung
Neudesign unserer Homepage: www.brivolt.at
responsives Design unter Beibehaltung unserer Logos bzw. Schriften und Farben( Logo kann gerne dezent verändert werden, aber die Charakteristik und Wiedererkennung muss bleiben ), gerne auch mit Webprogrammierung (CMS) welche aber separat ausgeschrieben/verhandelt wird. Seite soll komplett in HTML werden, technisch am Stand der Zeit mit allen Features die eine moderne HP haben soll.
Slogan "...damit Ihr Computer macht was er soll " wurde bisher schon oft verwendet und sollte wenn möglich eventuell untergebracht werden, gerne animiert.
Im Anhang einige bisher verwendete Grafiken zur Orientierung was bisher schon in Verwendung ist / war. (Bei Bedarf kann mehr geliefert werden)
Das Design sollte Kompetenz, Seriosität, renommiertes Unternehmen vermitteln. Kein Onlineshop momentan geplant. Schwerpunkt Reparatur/Wartung/Dienstleistung mit Ziel der Neukundengewinnung und Info für bestehende Kunden.
Grunddesign der Startseite, bei Bedarf je nach Designvorschlag auch Unterseite / Kontaktformular gerne im Direktauftrag, bei gefallen.

```html
<!DOCTYPE html>
<html lang="de">
<head>
<meta charset="utf-8">
<title>Brivolt – Computersysteme</title>
<link rel="stylesheet" href="https://fonts.googleapis.com/css2?family=Ubuntu:wght@400;500&family=Noto+Sans:ital,wght@0,400;1,400&display=swap">
<style>
  :root {
    --green: #62ad2a;
    --orange: #ff7a12;
    --ink: #3c3c3c;
    --muted: #8a8a8a;
    --rule: #dcdcdc;
    --grey-band: #ebebeb;
    --white: #ffffff;
    --hero-dark: #0c1620;
    --hero-mid: #1f3648;
  }
  * { box-sizing: border-box; margin: 0; padding: 0; }
  html, body { width: 1200px; height: 1071px; overflow: hidden; }
  body { position: relative; background: var(--white); font-family: "Noto Sans", sans-serif; color: var(--muted); }
  .abs { position: absolute; }
  .nowrap { white-space: nowrap; }
  .heading { font-family: "Ubuntu", sans-serif; font-weight: 400; color: var(--ink); }

  /* hero */
  .hero-image { left: 0; top: 0; width: 1200px; height: 397px;
    background: radial-gradient(ellipse at 50% 45%, var(--hero-mid) 0%, #142635 45%, var(--hero-dark) 100%); }
  .topbar { left: 0; top: 0; width: 1200px; height: 32px; background: rgba(255,255,255,0.93); border-bottom: 1px solid var(--green); }
  .logo { left: 208px; top: 7px; font-family: "Ubuntu", sans-serif; font-weight: 500; font-size: 20px; letter-spacing: 1px; color: #2a2a2a; }
  .nav { top: 11px; font-family: "Ubuntu", sans-serif; font-size: 9px; color: #555; }
  .nav.active { color: var(--green); }
  .hero-title { left: 0; width: 1200px; top: 152px; text-align: center; font-family: "Ubuntu", sans-serif; font-weight: 400; font-size: 20px; color: var(--green); }
  .hero-sub { left: 0; width: 1200px; top: 182px; text-align: center; font-family: "Ubuntu", sans-serif; font-size: 11.5px; line-height: 16.5px; color: var(--white); }
  .cta { left: 537px; top: 236px; width: 125px; height: 25px; background: var(--orange); color: var(--white);
    font-family: "Ubuntu", sans-serif; font-size: 11px; line-height: 25px; text-align: center; }

  .slogan-band { left: 0; top: 397px; width: 1200px; height: 37px; background: var(--green); color: var(--white);
    font-family: "Ubuntu", sans-serif; font-size: 14px; line-height: 37px; text-align: center; }

  /* services */
  .service { top: 468px; width: 170px; margin-left: -85px; text-align: center; white-space: nowrap; }
  .service h3 { font-family: "Ubuntu", sans-serif; font-weight: 400; font-size: 14px; line-height: 18px; color: var(--ink); }
  .service h3 span { color: var(--green); }
  .service p { margin-top: 17px; font-size: 9px; line-height: 13.75px; color: #999; }
  .service p b { font-weight: 400; color: var(--ink); }
  .service a { display: block; margin-top: 9px; font-size: 9px; color: var(--green); text-decoration: none; }
  .v-rule { width: 1px; background: var(--rule); }

  /* about + contact */
  .about-band { left: 0; top: 606px; width: 1200px; height: 233px; background: var(--grey-band); border-top: 1px solid #ddd; border-bottom: 1px solid #ddd; }
  .section-title { font-size: 14px; }
  .about-title { left: 200px; top: 642px; color: var(--muted); }
  .about-title b { font-weight: 500; color: #333; }
  .about-text { left: 200px; top: 676px; font-size: 9px; line-height: 13.75px; white-space: nowrap; }
  .about-text p + p { margin-top: 13.75px; }
  .contact-title { left: 850px; top: 642px; }
  .contact-list { left: 850px; top: 678px; font-size: 9px; line-height: 10.5px; }
  .contact-list dt { color: var(--ink); }
  .contact-list dd { margin-bottom: 6px; }
  .contact-list .inline dt { display: inline; }
  .contact-list .inline dd { display: inline; margin: 0; }

  /* testimonials + newsletter */
  .testi-title { left: 200px; top: 868px; }
  .testimonial { left: 200px; width: 465px; white-space: nowrap; }
  .avatar { position: absolute; left: 0; top: 0; width: 38px; height: 38px; background: linear-gradient(#f2f2f2, #cfcfcf); border: 1px solid #e2e2e2; }
  .testimonial p { margin-left: 48px; font-size: 9px; line-height: 13.75px; }
  .testimonial cite { display: block; margin-left: 48px; font-size: 9px; line-height: 13.75px; color: var(--ink); }
  .h-rule { height: 1px; background: var(--rule); }
  .news-title { left: 725px; top: 868px; }
  .news-lead { left: 725px; top: 903px; font-size: 9px; }
  .email-field { left: 725px; top: 925px; width: 170px; height: 19px; border: 1px solid #d8d8d8; font-size: 9px; font-style: italic; color: #b5b5b5; padding-left: 7px; line-height: 17px; }
  .subscribe { left: 906px; top: 925px; width: 87px; height: 19px; background: var(--green); color: var(--white); font-family: "Ubuntu", sans-serif; font-size: 11px; line-height: 19px; text-align: center; }
  .social-title { left: 725px; top: 960px; }
  .social { top: 986px; width: 19px; height: 19px; }

  .footer-nav { top: 1050px; font-family: "Ubuntu", sans-serif; font-size: 9px; color: #a8a8a8; }
  .footer-logo { left: 932px; top: 1046px; font-family: "Ubuntu", sans-serif; font-weight: 500; font-size: 8px; color: #888; }
</style>
</head>
<body>
  <div class="abs hero-image" role="img" aria-label="Nahaufnahme einer Computer-Hauptplatine mit CPU-Sockel in dunklem Blau"></div>
  <header>
    <div class="abs topbar"></div>
    <div class="abs logo">BRIVOLT</div>
    <nav>
      <span class="abs nav active" style="left:722px">Home</span>
      <span class="abs nav" style="left:767px">About us</span>
      <span class="abs nav" style="left:822px">Services</span>
      <span class="abs nav" style="left:876px">Blog</span>
      <span class="abs nav" style="left:914px">Contact us</span>
    </nav>
  </header>

  <h1 class="abs hero-title">Herzlich willkommen!</h1>
  <p class="abs hero-sub">Sie suchen einen kompetenten Partner in Sachen Hardware, Software, Computerreparaturen ...<br>mit persönlicher Beratung und Vorort-Service?</p>
  <div class="abs cta">CONTACT US</div>

  <div class="abs slogan-band">Damit ihr computer macht was er soll</div>

  <section>
    <div class="abs service" style="left:262px"><h3>Bri<span>Mobil</span></h3><p>Ob Sie die Lieferung und<br>Inbetriebnahme eines neuen<br>PC´s oder einfach eine ...</p><a>read more</a></div>
    <div class="abs v-rule" style="left:346px;top:472px;height:97px"></div>
    <div class="abs service" style="left:429px"><h3>Bri<span>Beratung</span></h3><p>Die professionelle Betreuung<br>und Beratung des<br>Kunden wird uns durch ...</p><a>read more</a></div>
    <div class="abs v-rule" style="left:508px;top:472px;height:97px"></div>
    <div class="abs service" style="left:594px"><h3>Bri<span>Premium</span></h3><p>Wenn der Geschäftsablauf ihres<br>Unternehmens von<br>der Verfügbarkeit der EDV ...</p><a>read more</a></div>
    <div class="abs v-rule" style="left:677px;top:472px;height:97px"></div>
    <div class="abs service" style="left:760px"><h3>Bri<span>Reparatur</span></h3><p>Wir überprüfen, reparieren und<br>erweitern Computer<br>und Peripheriegeräte von ...</p><a>read more</a></div>
    <div class="abs v-rule" style="left:849px;top:472px;height:97px"></div>
    <div class="abs service" style="left:927px"><h3>Bri<span>Recycling</span></h3><p><b>Nein,</b>denn durch moderne<br>Recyclingverfahren können<br>über 50 Prozent der ...</p><a>read more</a></div>
  </section>

  <div class="abs about-band"></div>
  <h2 class="abs heading section-title about-title">About <b>BRIVOLT</b></h2>
  <div class="abs about-text">
    <p>Lorem Ipsum is simply dummy text of the printing and typesetting industry. Lorem Ipsum has been the industry's standard<br>dummy text ever since the 1500s, when an unknown printer took a galley of type and scrambled it to make a type specimen<br>book.</p>
    <p>It has survived not only five centuries, but also the leap into electronic typesetting, remaining essentially unchanged.</p>
    <p>It was popularised in the 1960s with the release of Letraset sheets containing Lorem Ipsum passages, and more recently with<br>desktop publishing software like Aldus PageMaker including versions of Lorem Ipsum.</p>
  </div>
  <div class="abs v-rule" style="left:802px;top:653px;height:135px"></div>
  <h2 class="abs heading section-title contact-title">Contact</h2>
  <dl class="abs contact-list">
    <dt>Brivolt - Computersysteme</dt>
    <dd>Lindenweg 14<br>A-6830 Rankwil</dd>
    <dt>Hours of Operation</dt>
    <dd>Mon - Fri &nbsp;&nbsp;13.30 &nbsp;- 19.00</dd>
    <div class="inline"><dt>Phone:</dt> <dd>&nbsp;05522 / 71840</dd></div>
    <div class="inline" style="margin-bottom:6px"><dt>Fax:</dt> <dd>00 987 654 321</dd></div>
    <div class="inline"><dt>Email:</dt> <dd>office@brivolt.at</dd></div>
  </dl>

  <h2 class="abs heading section-title testi-title">Testamonials</h2>
  <div class="abs testimonial" style="top:907px">
    <div class="avatar" role="img" aria-label="Porträtfoto eines Kunden"></div>
    <p>Lorem Ipsum is simply dummy text of the printing and typesetting industry. Lorem Ipsum has<br>been the industry's standard dummy text ever since the 1500s.</p>
    <cite>Lukas Berner</cite>
  </div>
  <div class="abs h-rule" style="left:200px;top:957px;width:465px"></div>
  <div class="abs testimonial" style="top:969px">
    <div class="avatar" role="img" aria-label="Porträtfoto eines Kunden"></div>
    <p>Lorem Ipsum is simply dummy text of the printing and typesetting industry. Lorem Ipsum has<br>been the industry's standard dummy text ever since the 1500s.</p>
    <cite>Felix Hartmann</cite>
  </div>
  <div class="abs v-rule" style="left:694px;top:872px;height:133px"></div>

  <h2 class="abs heading section-title news-title">Newslatter</h2>
  <p class="abs news-lead">Get our exclusive offers:</p>
  <div class="abs email-field">Enter your email</div>
  <div class="abs subscribe">Subscribe</div>
  <h2 class="abs heading section-title social-title">Social network</h2>
  <div class="abs social" style="left:725px;background:#3b5a9a"></div>
  <div class="abs social" style="left:750px;background:#2ea3dd"></div>
  <div class="abs social" style="left:775px;background:#d44132"></div>
  <div class="abs social" style="left:800px;background:#c4302b"></div>

  <footer>
    <div class="abs h-rule" style="left:200px;top:1038px;width:800px"></div>
    <span class="abs footer-nav" style="left:225px">Home</span>
    <span class="abs footer-nav" style="left:269px">About us</span>
    <span class="abs footer-nav" style="left:325px">Services</span>
    <span class="abs footer-nav" style="left:379px">Blog</span>
    <span class="abs footer-nav" style="left:417px">Contact us</span>
    <span class="abs footer-logo">BRIVOLT</span>
  </footer>
</body>
</html>
```